Tranquil Harbor Yoga, meditation & wellness

I teach kundalini yoga and meditation classes.
I have adult beginner classes, seniors classes, family yoga classes, kids yoga classes
I also offer events like cacao ceremony, full moon ceremony, and retreats

Professional, and simple website that is easy to navigate, and easy for me to update, change.

Target Market(s)

all ages

Industry/Entity Type

Health And Wellness

Coding

Coded - Design and coding required

Number of Pages Required

5+ page

Font styles to use
Decorative

Colors
cedeed
eedded
e4daeb
fbd4d5
fee3d4

Requirements
Must have
• tabs required: about, contact, events, classes, blog,
• I would like to link my facebook page & instagram accounts to the website
Nice to have
• I would like my clients to be able to register for classes and events from my website
• I would like to have a "shop" option in the future, for some items that I have for sale

```html
<!DOCTYPE html>
<html lang="en">
<head>
<meta charset="utf-8">
<title>Tranquil Harbor – About &amp; Register</title>
<link href="https://fonts.googleapis.com/css2?family=Patrick+Hand+SC&family=Open+Sans:wght@400;600;700&display=swap" rel="stylesheet">
<style>
:root{
  --backdrop:#e8e8e8;
  --page:#ffffff;
  --ink:#2b2b2b;
  --text:#555555;
  --muted:#888888;
  --lilac:#c79be0;
  --lilac-soft:#ded0e8;
  --rule:#d0d0d0;
  --field:#bdbdbd;
  --sky-top:#bfe3e4;
  --sky-mid:#e6eeec;
  --sea:#b9c7c3;
}
*{margin:0;padding:0;box-sizing:border-box}
html,body{width:1162px;height:1200px;overflow:hidden;background:var(--backdrop);font-family:"Open Sans",sans-serif;color:var(--text)}
.page{position:absolute;background:var(--page);box-shadow:0 1px 4px rgba(0,0,0,.08);overflow:hidden}
.page--about{left:102px;top:138px;width:449px;height:924px}
.page--register{left:612px;top:138px;width:449px;height:544px}
.abs{position:absolute}
.heading{font-family:"Patrick Hand SC",cursive;color:var(--ink);font-weight:400;letter-spacing:1px}

/* hero */
.hero{position:absolute;left:0;top:0;width:449px;height:170px;background:linear-gradient(180deg,var(--sky-top) 0%,var(--sky-mid) 48%,#d4dedb 62%,var(--sea) 100%)}
.hero__figure{position:absolute;left:180px;top:40px;width:90px;height:130px;background:linear-gradient(180deg,rgba(240,240,236,.0),rgba(240,240,236,.75));border-radius:45px 45px 8px 8px}
.brand{position:absolute;left:30px;top:38px;width:116px;text-align:center;font-family:"Open Sans",sans-serif;font-weight:400;font-size:10px;letter-spacing:3px;color:var(--ink);line-height:14px}
.brand__dot{display:block;width:10px;height:10px;border-radius:50%;background:#f2b9c6;margin:0 auto 5px}
.topbar{position:absolute;top:14px;left:173px;display:flex;align-items:center;gap:4px;font-size:5.6px;color:var(--ink)}
.topbar svg{width:6px;height:6px;fill:var(--lilac)}
.topbar__sep{margin:0 4px}
.pill{position:absolute;top:9px;height:16px;border:1px solid #8a8a8a;border-radius:9px;font-size:5.8px;font-weight:700;color:var(--ink);display:flex;align-items:center;justify-content:center;gap:2px;background:rgba(255,255,255,.25)}
.pill--shop{left:319px;width:38px}
.pill--register{left:359px;width:47px}
.nav{position:absolute;top:35px;left:201px;display:flex;gap:0;font-size:6px;color:var(--ink);letter-spacing:.2px}
.nav span{margin-right:13px}
.nav .is-active{color:var(--lilac)}
.nav svg{width:6px;height:6px;margin-top:1px}
.hero__title{position:absolute;left:0;right:0;top:88px;text-align:center;font-family:"Patrick Hand SC",cursive;font-size:40px;color:#fff;letter-spacing:3px;text-shadow:0 1px 2px rgba(0,0,0,.25)}
.dots{position:absolute;top:140px;left:0;right:0;display:flex;justify-content:center;gap:2px}
.dots i{width:5px;height:5px;border-radius:50%;border:1px solid #fff}
.dots i:first-child{background:#fff}

/* about */
.portrait{left:42px;top:202px;width:136px;height:136px;border-radius:50%;border:2px solid #fff;box-shadow:0 0 0 1px #e6e6e6;background:radial-gradient(circle at 50% 45%,#d8a789 0%,#a8714e 35%,#3f4a44 75%)}
.bio__name{left:203px;top:216px;font-size:20px}
.bio__text{left:205px;top:246px;width:200px;font-size:5.5px;line-height:9.2px}
.bio__text p{margin-bottom:9px}
.divider{height:1px;background:var(--rule)}
.about-divider{left:42px;top:371px;width:365px}
.col{width:116px;top:404px}
.col h3{font-size:12px;line-height:14px;margin-bottom:17px;font-family:"Patrick Hand SC",cursive;color:var(--ink);font-weight:400;letter-spacing:1px}
.col p{font-size:5.5px;line-height:10px;padding-left:2px}

/* contact */
.contact{left:0;top:598px;width:449px;height:198px;background:var(--lilac-soft)}
.contact__photo{position:absolute;left:0;top:0;width:219px;height:198px;background:linear-gradient(135deg,#7d8a80 0%,#d9d6cf 45%,#eeeae2 70%,#5f6a62 100%)}
.contact__title{position:absolute;left:242px;top:33px;font-family:"Patrick Hand SC",cursive;color:#fff;font-size:17px;letter-spacing:2px}
.field{position:absolute;background:#fff;font-size:5.4px;color:var(--ink);padding:5px 6px}
.contact .field{width:81px;height:16px}
.submit{position:absolute;left:242px;top:148px;width:48px;height:17px;border:1px solid #fff;border-radius:9px;color:#fff;font-size:6px;font-weight:700;display:flex;align-items:center;justify-content:center;letter-spacing:.5px}

/* footer */
.footer{left:0;width:449px;text-align:center}
.social{display:flex;justify-content:center;gap:1px}
.social i{width:20px;height:20px;border-radius:50%;border:1px solid #c6c6c6}
.footer__line{margin-top:10px;font-size:5.6px;color:var(--text);display:flex;justify-content:center;align-items:center;gap:3px}
.footer__line svg{width:6px;height:6px;fill:#c6c6c6}
.footer__links{margin-top:7px;font-size:5.4px}
.footer__links span{margin:0 4px}
.footer__copy{margin-top:8px;font-size:5.4px}

/* register */
.reg__title{left:0;width:449px;text-align:center;top:200px;font-size:19px}
.reg__signin{left:0;width:449px;text-align:center;top:229px;font-size:6.8px;color:var(--ink)}
.reg__signin a{color:var(--lilac);text-decoration:underline}
.label{font-size:6.2px;color:var(--ink)}
.reg .field{width:133px;height:18px;border:1px solid var(--field);padding:0 7px;display:flex;align-items:center}
.reg .field svg{width:6px;height:6px;fill:#999}
.agree{left:0;width:449px;top:343px;display:flex;justify-content:center;align-items:center;gap:5px;font-size:5.8px;color:var(--ink)}
.agree i{width:7px;height:7px;border:1px solid #777;border-radius:1px}
.create{left:182px;top:372px;width:85px;height:23px;border-radius:12px;background:var(--lilac);color:#fff;font-size:6.6px;font-weight:700;display:flex;align-items:center;justify-content:center;letter-spacing:.3px}
.reg-divider{left:41px;top:436px;width:367px}
</style>
</head>
<body>

<!-- About page -->
<section class="page page--about">
  <header class="hero">
    <div class="hero__figure" role="img" aria-label="Photo of a woman meditating in lotus pose by the sea"></div>
    <div class="brand"><span class="brand__dot"></span>TRANQUIL<br>HARBOR</div>
    <div class="topbar">
      <svg viewBox="0 0 10 10"><path d="M2 1l2 0 1 2.5-1.3 1a5 5 0 0 0 2.8 2.8l1-1.3L10 7v2c0 .6-.4 1-1 1A9 9 0 0 1 0 1c0-.6.4-1 1-1z"/></svg>
      <span>555-013-2846</span><span class="topbar__sep">|</span>
      <svg viewBox="0 0 10 8"><path d="M0 0h10v8H0z"/></svg>
      <span>tranquilharbor@mail.com</span>
    </div>
    <div class="pill pill--shop">&#128722;&#xFE0E;SHOP</div>
    <div class="pill pill--register">&#9998; REGISTER</div>
    <nav class="nav"><span>HOME</span><span class="is-active">ABOUT</span><span>CONTACT</span><span>EVENTS</span><span>CLASSES</span><span>BLOG</span>
      <svg viewBox="0 0 10 10"><circle cx="4" cy="4" r="3" fill="none" stroke="#2b2b2b" stroke-width="1.6"/><path d="M6 6l3 3" stroke="#2b2b2b" stroke-width="1.8"/></svg></nav>
    <h1 class="hero__title">ABOUT</h1>
    <div class="dots"><i></i><i></i><i></i><i></i></div>
  </header>

  <div class="abs portrait" role="img" aria-label="Portrait of the yoga teacher"></div>
  <h2 class="abs heading bio__name">LENA (DEV PREM KAUR)</h2>
  <div class="abs bio__text">
    <p>I have been practicing yoga for about 5 years, I began practicing Kundalini yoga 2 years ago, and it ignited a complete transformation of mind, body and spirit. I knew that I would go on to teach this lineage.</p>
    <p>I'm also a nurse part time with the CVHS, my 18 years of health care experience has been invaluable. My most important job of all is wife, mother and home educator to my four daughters, ages 9-4 years.</p>
  </div>
  <div class="abs divider about-divider"></div>

  <div class="abs col" style="left:42px">
    <h3>FOR YOUR<br>COMFORT</h3>
    <p>Wear loose fitted clothing that is comfortable moves with you. You may wish to wear layers as your body temperature will likely change during practice, warming during the more active phases and cooling during the restful phases. Please bring a blanket for extra comfort during the relaxation and meditation portion of the class.</p>
  </div>
  <div class="abs col" style="left:168px">
    <h3>YOU CONTRIBUTE TO<br>THE EXPERIENCE</h3>
    <p>Please refrain from wearing perfume or other strong scents to class. Turn off cell phones or make them completely silent, in other words no vibration. Remove shoes in the vestibule before entering the practice area. Be on time to class. If you intend to miss a class please email (tranquilharboryoga@mail.com) or TEXT: 555-013-2846</p>
  </div>
  <div class="abs col" style="left:297px">
    <h3>YOUR<br>WELLBEING</h3>
    <p>You are responsible to make me aware of any medical conditions or physical concerns you may have in general and on the day of your class. I will offer guidance and accommodations based on this knowledge. Chairs and props are available to assist you whenever you need them. It is your responsibility to keep yourself safe and injury free. Use your own wisdom and knowledge of your body to make adjustments during your practice. This is YOUR practice and is intended to benefit you and address your particular needs. You always have a choice. You decide.</p>
  </div>

  <section class="abs contact">
    <div class="contact__photo" role="img" aria-label="Photo of the teacher playing crystal singing bowls"></div>
    <h2 class="contact__title">GET IN TOUCH</h2>
    <div class="field" style="left:242px;top:62px">First Name</div>
    <div class="field" style="left:326px;top:62px">Last Name</div>
    <div class="field" style="left:242px;top:82px">Email Address</div>
    <div class="field" style="left:326px;top:82px">Phone Number</div>
    <div class="field" style="left:242px;top:102px;width:165px;height:31px">Message</div>
    <div class="submit">SUBMIT</div>
  </section>

  <footer class="abs footer" style="top:836px">
    <div class="social" aria-label="Social links"><i></i><i></i></div>
    <div class="footer__line">
      <svg viewBox="0 0 8 10"><path d="M4 0a4 4 0 0 1 4 4c0 3-4 6-4 6S0 7 0 4a4 4 0 0 1 4-4z"/></svg><span>42 Linden Row Harbourside VIC 3190 Australia</span><span>|</span>
      <svg viewBox="0 0 10 10"><path d="M2 1l2 0 1 2.5-1.3 1a5 5 0 0 0 2.8 2.8l1-1.3L10 7v2c0 .6-.4 1-1 1A9 9 0 0 1 0 1c0-.6.4-1 1-1z"/></svg><span>555-013-2846</span><span>|</span>
      <svg viewBox="0 0 10 8"><path d="M0 0h10v8H0z"/></svg><span>tranquilharbor@mail.com</span>
    </div>
    <div class="footer__links">Help<span>|</span>FAQ<span>|</span>Support<span>|</span>Sitemap<span>|</span>Terms Of Use<span>|</span>Privacy Statement</div>
    <div class="footer__copy">Tranquil Harbor Yoga © 2018 All rights reserved.</div>
  </footer>
</section>

<!-- Register page -->
<section class="page page--register reg">
  <header class="hero">
    <div class="hero__figure" role="img" aria-label="Photo of a woman meditating in lotus pose by the sea"></div>
    <div class="brand"><span class="brand__dot"></span>TRANQUIL<br>HARBOR</div>
    <div class="topbar">
      <svg viewBox="0 0 10 10"><path d="M2 1l2 0 1 2.5-1.3 1a5 5 0 0 0 2.8 2.8l1-1.3L10 7v2c0 .6-.4 1-1 1A9 9 0 0 1 0 1c0-.6.4-1 1-1z"/></svg>
      <span>555-013-2846</span><span class="topbar__sep">|</span>
      <svg viewBox="0 0 10 8"><path d="M0 0h10v8H0z"/></svg>
      <span>tranquilharbor@mail.com</span>
    </div>
    <div class="pill pill--shop">&#128722;&#xFE0E;SHOP</div>
    <div class="pill pill--register">&#9998; REGISTER</div>
    <nav class="nav"><span>HOME</span><span class="is-active">ABOUT</span><span>CONTACT</span><span>EVENTS</span><span>CLASSES</span><span>BLOG</span>
      <svg viewBox="0 0 10 10"><circle cx="4" cy="4" r="3" fill="none" stroke="#2b2b2b" stroke-width="1.6"/><path d="M6 6l3 3" stroke="#2b2b2b" stroke-width="1.8"/></svg></nav>
    <h1 class="hero__title">REGISTER</h1>
    <div class="dots"><i></i><i></i><i></i><i></i></div>
  </header>

  <h2 class="abs heading reg__title">REGISTRATION</h2>
  <p class="abs reg__signin">Already have an account? <a>Sign In</a></p>

  <span class="abs label" style="left:87px;top:256px">User Name</span>
  <span class="abs label" style="left:228px;top:256px">Email</span>
  <div class="abs field" style="left:87px;top:269px"><svg viewBox="0 0 10 10"><circle cx="5" cy="3" r="2.5"/><path d="M0 10c0-4 10-4 10 0z"/></svg></div>
  <div class="abs field" style="left:228px;top:269px"><svg viewBox="0 0 10 8"><path d="M0 0h10v8H0z"/></svg></div>

  <span class="abs label" style="left:87px;top:294px">Password</span>
  <span class="abs label" style="left:228px;top:294px">Re-enter Password</span>
  <div class="abs field" style="left:87px;top:306px"><svg viewBox="0 0 10 10"><path d="M1 5h8v5H1z"/><path d="M3 5V3a2 2 0 0 1 4 0v2" fill="none" stroke="#999" stroke-width="1.4"/></svg></div>
  <div class="abs field" style="left:228px;top:306px"><svg viewBox="0 0 10 10"><path d="M1 5h8v5H1z"/><path d="M3 5V3a2 2 0 0 1 4 0v2" fill="none" stroke="#999" stroke-width="1.4"/></svg></div>

  <div class="abs agree"><i></i><span>Do you agree to the User Agreement and Privacy Policy?</span></div>
  <div class="abs create">CREATE ACCOUNT</div>
  <div class="abs divider reg-divider"></div>

  <footer class="abs footer" style="top:458px">
    <div class="social" aria-label="Social links"><i></i><i></i></div>
    <div class="footer__line">
      <svg viewBox="0 0 8 10"><path d="M4 0a4 4 0 0 1 4 4c0 3-4 6-4 6S0 7 0 4a4 4 0 0 1 4-4z"/></svg><span>42 Linden Row Harbourside VIC 3190 Australia</span><span>|</span>
      <svg viewBox="0 0 10 10"><path d="M2 1l2 0 1 2.5-1.3 1a5 5 0 0 0 2.8 2.8l1-1.3L10 7v2c0 .6-.4 1-1 1A9 9 0 0 1 0 1c0-.6.4-1 1-1z"/></svg><span>555-013-2846</span><span>|</span>
      <svg viewBox="0 0 10 8"><path d="M0 0h10v8H0z"/></svg><span>tranquilharbor@mail.com</span>
    </div>
    <div class="footer__links">Help<span>|</span>FAQ<span>|</span>Support<span>|</span>Sitemap<span>|</span>Terms Of Use<span>|</span>Privacy Statement</div>
    <div class="footer__copy">Tranquil Harbor Yoga © 2018 All rights reserved.</div>
  </footer>
</section>

</body>
</html>
```